Corvane Supplies Business Card

Professional business card that stand out to our potential customers. Front and back with clean modern design

Industry/Entity Type

Oil and gas

Contact Information for Business Card

Name, address, website , office phone and cell number

Requirements
Must have
• Editable files for each employee

```html
<!DOCTYPE html>
<html lang="en">
<head>
<meta charset="utf-8">
<title>Corvane Supplies – Business Card</title>
<link rel="stylesheet" href="https://fonts.googleapis.com/css2?family=Montserrat:wght@600;700&family=Didact+Gothic&display=swap">
<style>
  :root{
    --board:#7d7474;
    --cyan:#03aed0;
    --red:#ff0000;
    --stone:#d8caca;
    --white:#ffffff;
    --ink:#2a2a2a;
    --rule:#555555;
  }
  html,body{margin:0;padding:0;overflow:hidden;background:var(--board);}
  .board{display:block;width:1200px;height:849px;}
  .board-bg{fill:var(--board);}
  .heading{font-family:"Montserrat",sans-serif;font-weight:700;fill:var(--white);}
  .side-label{font-family:"Montserrat",sans-serif;font-weight:600;fill:var(--white);font-size:60px;text-anchor:middle;}
  .fill-cyan{fill:var(--cyan);}
  .fill-red{fill:var(--red);}
  .fill-stone{fill:var(--stone);}
  .fill-white{fill:var(--white);}
  .stroke-white{stroke:var(--white);fill:none;}
  .card-shadow{filter:drop-shadow(0 2px 3px rgba(0,0,0,.35));}
  .brand-back{font-family:"Montserrat",sans-serif;font-weight:700;fill:var(--red);font-size:58px;text-anchor:middle;}
  .brand-front{font-family:"Montserrat",sans-serif;font-weight:700;fill:var(--ink);font-size:34px;text-anchor:middle;}
  .person-name{font-family:"Montserrat",sans-serif;font-weight:700;fill:var(--ink);font-size:50px;}
  .person-role{font-family:"Montserrat",sans-serif;font-weight:600;fill:var(--ink);font-size:25px;text-anchor:end;}
  .contact{font-family:"Didact Gothic",sans-serif;fill:var(--ink);font-size:27px;}
  .address{font-family:"Didact Gothic",sans-serif;fill:var(--ink);font-size:24px;}
  .divider{stroke:var(--rule);stroke-width:3;}
  .icon{fill:var(--rule);}
  .icon-line{stroke:var(--rule);fill:none;stroke-width:1.6;}
</style>
</head>
<body>
<svg class="board" viewBox="0 0 2296 1624" xmlns="http://www.w3.org/2000/svg">
  <defs>
    <clipPath id="card-clip"><rect width="948" height="542"/></clipPath>
  </defs>
  <rect class="board-bg" width="2296" height="1624"/>
  <text class="heading" x="150" y="95" font-size="56">Doublesided print bussiness card</text>

  <!-- Back of card -->
  <g class="card card-back" transform="translate(361 254)">
    <rect class="fill-stone card-shadow" width="948" height="542"/>
    <g clip-path="url(#card-clip)">
      <polygon class="fill-cyan" points="0,0 452,0 0,322"/>
      <line class="stroke-white" x1="0" y1="334" x2="472" y2="0" stroke-width="13"/>
      <polygon class="fill-red" points="948,222 948,542 500,542"/>
      <line class="stroke-white" x1="948" y1="208" x2="478" y2="542" stroke-width="13"/>
    </g>
    <text class="brand-back" x="487" y="290">CORVANE SUPPLIES</text>
  </g>
  <text class="side-label" x="793" y="852">back</text>

  <!-- Front of card -->
  <g class="card card-front" transform="translate(997 868)">
    <rect class="fill-white card-shadow" width="948" height="542"/>
    <g clip-path="url(#card-clip)">
      <polygon class="fill-red" points="0,0 948,0 948,22 535,22 520,30 0,30"/>
      <polygon class="fill-cyan" points="0,38 205,38 0,122"/>
      <polygon class="fill-cyan" points="385,36 600,32 498,75"/>
      <polygon class="fill-cyan" points="902,28 948,28 948,58"/>
      <polygon class="fill-red" points="0,398 185,500 0,500"/>
      <polygon class="fill-cyan" points="0,508 330,508 345,520 948,520 948,542 0,542"/>
      <polygon class="fill-red" points="900,515 948,463 948,515"/>
    </g>

    <!-- brand -->
    <rect class="fill-red" x="160" y="150" width="130" height="130"/>
    <text class="brand-front" x="210" y="360">CORVANE SUPPLIES</text>

    <line class="divider" x1="437" y1="175" x2="437" y2="370"/>

    <!-- person -->
    <text class="person-name" x="481" y="214" textLength="400" lengthAdjust="spacingAndGlyphs">DANIEL HARLOW</text>
    <text class="person-role" x="870" y="240">MARKETING MANAGER</text>

    <!-- contacts -->
    <g transform="translate(491 283)">
      <circle class="icon-line" r="10"/>
      <ellipse class="icon-line" rx="4.5" ry="10"/>
      <line class="icon-line" x1="-10" y1="0" x2="10" y2="0"/>
    </g>
    <text class="contact" x="510" y="292">www.corvanesupplies.com</text>
    <g transform="translate(481 313)">
      <rect class="icon" width="21" height="15"/>
      <polyline points="0,0 10.5,8 21,0" stroke="#fff" stroke-width="1.6" fill="none"/>
    </g>
    <text class="contact" x="510" y="330">sales@corvanesupplies.com</text>
    <g transform="translate(491 359)">
      <circle class="icon" r="11"/>
      <path d="M-5,-5 q0,10 10,10 l1,-3 -3,-2 -2,2 q-4,-2 -5,-5 l2,-2 -2,-3z" fill="#fff"/>
    </g>
    <text class="contact" x="510" y="368">(555) 204-7781</text>

    <!-- address -->
    <path class="icon" d="M410,487 q-9,0 -9,9 q0,7 9,19 q9,-12 9,-19 q0,-9 -9,-9z M410,492 a4,4 0 1 0 0.1,0z" fill-rule="evenodd"/>
    <text class="address" x="427" y="510">412 W. Larkspur Suite 5 Midland, Tx 79701</text>
  </g>
  <text class="side-label" x="1507" y="1473">front</text>
</svg>
</body>
</html>
```